Bright oak path business card

Bright oak path is a new online life insurance company providing instant quotes and policies to consumers.
Target Market(s)
Target market is both business to business as well as business to consumer
Can think out side of the box- We are an open minded bunch
Industry/Entity Type
Life Insurance
Requirements
Must have
- Our corporate Logo
Double sided
Website www.brightoakpath.com.au
Phone Number
Name & Position of each person etc.
Modern font

```html
<!DOCTYPE html>
<html lang="en">
<head>
<meta charset="utf-8">
<title>Bright oak path business card</title>
<link href="https://fonts.googleapis.com/css2?family=Jost:wght@400;500&family=Open+Sans:wght@400&display=swap" rel="stylesheet">
<style>
  :root {
    --ink: #231f20;
    --orange: #f08133;
    --paper: #ffffff;
    --edge: #b5b5b5;
  }
  * { margin: 0; padding: 0; box-sizing: border-box; }
  html, body { width: 1200px; height: 900px; overflow: hidden; background: var(--paper); }
  .canvas { position: relative; width: 1200px; height: 900px; }

  .card { position: absolute; width: 525px; height: 321px; }
  .card-front { left: 99px; top: 114px; background: var(--paper); border: 1px solid var(--edge); }
  .card-back { left: 583px; top: 472px; width: 524px; height: 320px; background: var(--orange); }

  .brand-name {
    position: absolute; left: 54px; top: 62px;
    font-family: "Jost", sans-serif; font-weight: 500;
    font-size: 74px; line-height: 0.92; letter-spacing: -2px;
    color: var(--ink);
  }
  .tagline {
    position: absolute; right: 44px; top: 228px;
    font-family: "Jost", sans-serif; font-weight: 400;
    font-size: 31px; letter-spacing: 0.5px;
    color: var(--orange);
  }

  .contact-ring { position: absolute; left: 0; top: 0; }
  .ring-address { font-family: "Jost", sans-serif; font-weight: 500; font-size: 18px; fill: var(--ink); }
  .ring-web { font-family: "Jost", sans-serif; font-weight: 400; font-size: 11px; fill: var(--ink); }
  .ring-tagline { font-family: "Jost", sans-serif; font-weight: 400; font-size: 26px; fill: var(--paper); letter-spacing: 1px; }

  .person { position: absolute; left: 16px; top: 252px; font-family: "Open Sans", sans-serif; color: var(--paper); font-size: 18px; line-height: 31px; }
  .person-position { padding-left: 2px; }
</style>
</head>
<body>
<div class="canvas">

  <section class="card card-front">
    <div class="brand-name">Bright oak<br>path</div>
    <div class="tagline">CLEAR. SIMPLE.</div>
  </section>

  <section class="card card-back">
    <svg class="contact-ring" width="524" height="320" viewBox="583 472 524 320">
      <defs>
        <path id="outer-ring" d="M955.3 635.6 A112 112 0 1 1 806.7 549.7"/>
        <path id="inner-ring" d="M915.5 629.3 A75 75 0 1 1 819.3 584.5"/>
      </defs>
      <text class="ring-address">
        <textPath href="#outer-ring" startOffset="6">Level 12, 48 Harbour Lane North Shore NSW</textPath>
      </text>
      <text class="ring-web">
        <textPath href="#inner-ring" startOffset="4">Ph 1300 555 010 | www.brightoakpath.com.au</textPath>
      </text>
      <text class="ring-tagline" x="850" y="648" text-anchor="middle">CLEAR.</text>
      <text class="ring-tagline" x="850" y="680" text-anchor="middle">SIMPLE.</text>
    </svg>
    <div class="person">
      <div class="person-name">Your Name</div>
      <div class="person-position">Position</div>
    </div>
  </section>

</div>
</body>
</html>
```